Powerpoint template for corporate presentations

Our company, MeridianQuillworks, has recently undertaken a re-branding overhaul for our website and corporate materials (color scheme, letterhead, biz cards). In support of this re-branding effort, we need a powerpoint template for corporate presentations that will reflect the look and feel of the website.

We would like to receive a powerpoint template that contains the following slide layouts:
- title slide
- section header slide
- content slide (title & content)
- closing/acknowledgement slide

The website design, colors, fonts and images are included as attachments for your reference.An example powerpoint template is included, if needed for your reference. We would like to see the icons and colors used to make the presentation more visually appealing.

Specific comments regarding the example ppt with content attached to this brief:
- the content slides seem a bit sparse and do not have much space for text/charts.
- For the content slides, a white/light background and dark text is still expected.
- For the section header and closing slides, we would like to see a layout more engaging than just the blue background. Note: a blue or colored background is acceptable for these slides so long as the text color has enough contrast to be visible.

```html
<!DOCTYPE html>
<html lang="en">
<head>
<meta charset="utf-8">
<title>Closing Slide</title>
<link rel="stylesheet" href="https://fonts.googleapis.com/css2?family=Arimo:wght@700&display=swap">
<style>
  :root {
    --slide-yellow: #ffe278;
    --glow-light: #ffeba8;
    --text-charcoal: #4d5057;
    --bar-blue: #17b2da;
    --bar-charcoal: #54565b;
    --bar-sky: #9adff7;
  }
  html, body {
    margin: 0;
    padding: 0;
    width: 1200px;
    height: 900px;
    overflow: hidden;
  }
  .slide {
    position: relative;
    width: 1200px;
    height: 900px;
    background: var(--slide-yellow);
    overflow: hidden;
    font-family: "Arimo", Arial, sans-serif;
  }
  .decor-area {
    position: absolute;
    left: 450px;
    top: 20px;
    width: 750px;
    height: 450px;
    background: radial-gradient(ellipse at 55% 40%, var(--glow-light) 0%, rgba(255, 235, 168, 0.6) 40%, rgba(255, 226, 120, 0) 75%);
  }
  .closing-title {
    position: absolute;
    left: 0;
    right: 0;
    top: 537px;
    margin: 0;
    text-align: center;
    font-weight: 700;
    font-size: 46px;
    line-height: 60px;
    color: var(--text-charcoal);
  }
  .accent-bar {
    position: absolute;
    left: 299px;
    right: 0;
    bottom: 0;
    height: 21px;
    display: flex;
  }
  .accent-bar__segment { flex: 1; }
  .accent-bar__segment--blue { background: var(--bar-blue); }
  .accent-bar__segment--charcoal { background: var(--bar-charcoal); }
  .accent-bar__segment--sky { background: var(--bar-sky); }
</style>
</head>
<body>
  <main class="slide">
    <div class="decor-area" role="img" aria-label="Decorative cluster of translucent light squares"></div>

    <h1 class="closing-title">Closing slide comes here</h1>

    <div class="accent-bar">
      <div class="accent-bar__segment accent-bar__segment--blue"></div>
      <div class="accent-bar__segment accent-bar__segment--charcoal"></div>
      <div class="accent-bar__segment accent-bar__segment--sky"></div>
    </div>
  </main>
</body>
</html>
```